Pals of Rusty Fundraiser Flyer for shelter dogs

Flyer for Fund Raiser for shelter and rescue dogsThis will be hosted by who we are calling Heroes First responders (Fire, Police, and EMS will be bartending raising money to help the shelter dogs).

I will be uploading a basic flyer I did but I don't like it, only showing for dates and words etc...

struggling to come up with something eye-catching related to the above.

We can keep the use of Heroes (spelled wrong on the flyer)but open for new ideas too and new title.

Target Market(s)

Animal lovers

Font styles to use
Serif
Sans Serif

Requirements
Must have
• the ties to first responders and dog rescue
• Must include First responder logo badges images. The image with the helping hands Maybe replace the badges with images of dogs or doggy paws something like that
• Must have a strong presence identifying and relating to first responders
• Images of first responders as well as even images of the first responder logos for fire department police department and EMS.
• The first responders are the ones hosting the event so we really want to raise them up and show their appreciation for the cause that is super important as well
• Title should read
• Guardians Guarding Mutts

```html
<!DOCTYPE html>
<html lang="en">
<head>
<meta charset="utf-8">
<title>Be a Hero, Save a Life – Pals of Rusty</title>
<link rel="stylesheet" href="https://fonts.googleapis.com/css2?family=Days+One&family=Oswald:wght@400;500;700&family=Montserrat:wght@400;500;600;700&display=swap">
<style>
  :root {
    --paper: #f7f7f5;
    --ink: #111111;
    --red: #e8202a;
    --grey-title: #7b7b7b;
    --grey-soft: #e2e2e0;
    --fur-light: #ecdcb8;
    --fur-deep: #c9a66b;
  }
  * { margin: 0; padding: 0; box-sizing: border-box; }
  html, body { width: 984px; height: 1200px; overflow: hidden; background: var(--paper); }
  .flyer { position: relative; width: 984px; height: 1200px; overflow: hidden; background: var(--paper); font-family: "Montserrat", sans-serif; color: var(--ink); }

  .frame { position: absolute; inset: 0; }
  .paw-spot { position: absolute; width: 100px; height: 100px; border-radius: 22px; background: var(--grey-soft); }
  .paw-spot.top-left { left: 34px; top: 24px; }
  .paw-spot.top-right { left: 850px; top: 24px; }
  .paw-spot.bottom-left { left: 44px; top: 650px; }
  .paw-spot.bottom-right { left: 842px; top: 650px; }

  .hero-heart { position: absolute; left: 240px; top: 14px; width: 508px; height: 440px; }
  .dog-photo { position: absolute; left: 350px; top: 96px; width: 290px; height: 340px;
    border-radius: 48% 48% 50% 50% / 40% 40% 60% 60%;
    background: radial-gradient(ellipse at 50% 40%, var(--fur-light), var(--fur-deep)); }

  .headline { position: absolute; left: 0; width: 984px; text-align: center; font-family: "Days One", sans-serif;
    font-size: 80px; color: var(--grey-title); -webkit-text-stroke: 3px #3a3a3a; line-height: 1; white-space: nowrap; }
  .headline.line-one { top: 462px; }
  .headline.line-two { top: 588px; }

  .event-date { position: absolute; left: 76px; top: 786px; display: flex; align-items: center; white-space: nowrap; }
  .event-date .day { font-family: "Oswald", sans-serif; font-weight: 700; font-size: 100px; color: var(--red);
    -webkit-text-stroke: 2px var(--ink); line-height: 1; letter-spacing: -1px; }
  .event-date .divider { width: 3px; height: 62px; background: var(--ink); margin: 12px 18px 0 20px; }
  .event-date .time { font-family: "Oswald", sans-serif; font-weight: 400; font-size: 86px; line-height: 1; margin-top: 8px; }

  .venue-bar { position: absolute; left: 75px; top: 916px; width: 491px; height: 36px; background: var(--red);
    color: #fff; font-size: 24px; line-height: 36px; padding-left: 10px; white-space: nowrap; }
  .venue-bar strong { font-weight: 700; margin-left: 6px; letter-spacing: 0.5px; }

  .invite { position: absolute; left: 75px; top: 966px; width: 492px; font-size: 15.4px; line-height: 22.5px;
    text-align: justify; font-weight: 500; }
  .invite b { font-weight: 700; }

  .social { position: absolute; left: 80px; list-style: none; display: flex; align-items: center; gap: 14px;
    font-weight: 600; font-size: 16px; }
  .social.first { top: 1074px; }
  .social.second { top: 1122px; }
  .social .dot { width: 40px; height: 40px; border-radius: 50%; background: var(--ink); border: 3px solid var(--red); }

  .responder-badges { position: absolute; left: 320px; top: 1072px; width: 256px; height: 82px; }

  .shelter-name { position: absolute; left: 630px; top: 1078px; width: 300px; text-align: center; }
  .shelter-name .name-row { display: flex; align-items: center; justify-content: center; gap: 12px; }
  .shelter-name .mark { width: 40px; height: 40px; border-radius: 50%; background: var(--red); }
  .shelter-name .name { font-size: 28px; font-weight: 600; color: #333; }
  .shelter-name .subtitle { margin-top: 4px; font-size: 12.5px; font-weight: 600; color: #555; letter-spacing: 0.3px; }

  .web-tag { position: absolute; left: 628px; top: 1155px; width: 264px; height: 23px; background: var(--red);
    color: #fff; font-size: 13.5px; font-weight: 600; line-height: 23px; text-align: center; }

  .base-band { position: absolute; left: 0; bottom: 0; width: 984px; height: 14px; background: var(--red); }
</style>
</head>
<body>
<main class="flyer">

  <div class="paw-spot top-left" role="img" aria-label="Decorative paw print"></div>
  <div class="paw-spot top-right" role="img" aria-label="Decorative paw print"></div>
  <div class="paw-spot bottom-left" role="img" aria-label="Decorative paw print"></div>
  <div class="paw-spot bottom-right" role="img" aria-label="Decorative paw print"></div>

  <svg class="frame" width="984" height="1200" viewBox="0 0 984 1200" aria-hidden="true">
    <g fill="var(--ink)">
      <rect x="158" y="70" width="84" height="6" rx="3"/>
      <rect x="168" y="84" width="74" height="6" rx="3"/>
      <rect x="745" y="70" width="84" height="6" rx="3"/>
      <rect x="745" y="84" width="74" height="6" rx="3"/>
      <rect x="70" y="170" width="7" height="460" rx="3"/>
      <rect x="96" y="160" width="7" height="470" rx="3"/>
      <rect x="870" y="160" width="7" height="470" rx="3"/>
      <rect x="896" y="170" width="7" height="460" rx="3"/>
      <rect x="160" y="698" width="670" height="8" rx="4"/>
      <rect x="170" y="716" width="650" height="8" rx="4"/>
    </g>
  </svg>

  <svg class="hero-heart" viewBox="0 0 508 440" aria-hidden="true">
    <path d="M254 440 C120 330 6 250 6 130 C6 50 70 4 140 4 C195 4 236 40 254 78 C272 40 313 4 368 4 C438 4 502 50 502 130 C502 250 388 330 254 440 Z" fill="var(--ink)"/>
    <path d="M254 424 C128 320 18 246 18 140 C18 72 74 34 136 34 C188 34 230 66 254 104 C278 66 320 34 372 34 C434 34 490 72 490 140 C490 246 380 320 254 424 Z" fill="var(--red)"/>
  </svg>
  <div class="dog-photo" role="img" aria-label="Photo of a smiling golden retriever puppy"></div>

  <h1 class="headline line-one">BE A HERO</h1>
  <h2 class="headline line-two">SAVE A LIFE</h2>

  <div class="event-date">
    <span class="day">AUG 15,2019</span>
    <span class="divider"></span>
    <span class="time">6-10 PM</span>
  </div>

  <div class="venue-bar">Hosted at - <strong>THE COVE CLUB</strong></div>

  <p class="invite"><b>"JOIN ............ OF FUN"</b> Come spend an evening with our Celebrity Bartenders and help some pups in need. Our local men and women in uniform will be pouring drinks and raising awareness of adoption.</p>

  <ul class="social first"><li class="dot"></li><li>palsofrustymcdp</li></ul>
  <ul class="social second"><li class="dot"></li><li>pormcdp</li></ul>

  <svg class="responder-badges" viewBox="0 0 256 82" role="img" aria-label="Police, fire and EMS badges">
    <path d="M2 6 L34 0 L66 6 L66 40 C66 62 50 76 34 82 C18 76 2 62 2 40 Z" fill="var(--ink)"/>
    <circle cx="121" cy="41" r="39" fill="var(--ink)"/>
    <rect x="174" y="2" width="80" height="78" rx="6" fill="var(--ink)"/>
  </svg>

  <div class="shelter-name">
    <div class="name-row"><span class="mark"></span><span class="name">Pals of Rusty</span></div>
    <div class="subtitle">MAPLE COUNTY DOG POUND</div>
  </div>
  <div class="web-tag">www.palsofrustyshelter.org</div>

  <div class="base-band"></div>
</main>
</body>
</html>
```